Coffeeshop menu for filter tip

We want to have a cannabis (coffeeshop) menu in the size 25mm wide x 60mm wide. Some examples attached.

it must have the following text:
Menu

WEED p/g
Vortigan €16
Tangerosa €14
Dusk Rover €14
Mangolina €16
Ultra Fern €14
Amber Hermit €14

HASH p/g
Nepali Bronze €12
Velvet Ember€11
Cedar Pine €14
Red Fable €10

Target Market(s)

tourist in Amsterdam

Requirements
Nice to have
• cannabis sign leaf
• No Cigarettes allowed symbol

```html
<!DOCTYPE html>
<html lang="en">
<head>
<meta charset="utf-8">
<title>Cannabis Menu</title>
<link href="https://fonts.googleapis.com/css2?family=Pinyon+Script&family=Montserrat:ital,wght@0,800;1,700&display=swap" rel="stylesheet">
<style>
  :root {
    --page: #ececec;
    --panel-top: #1b2024;
    --panel-mid: #1f2429;
    --panel-low: #2a3142;
    --yellow: #f2ec1f;
    --white: #ffffff;
    --ink: #111111;
    --leaf: #1f3a2c;
    --berry-red: #5a3440;
    --berry-blue: #2c3552;
  }
  * { margin: 0; padding: 0; box-sizing: border-box; }
  html, body { width: 960px; height: 1200px; overflow: hidden; background: var(--page); }
  .menu-panel {
    position: absolute; left: 230px; top: 0; width: 500px; height: 1200px; overflow: hidden;
    background: linear-gradient(180deg, var(--panel-top) 0%, var(--panel-mid) 60%, var(--panel-low) 100%);
    font-family: "Montserrat", Arial, sans-serif;
  }
  .leaf-art {
    position: absolute; right: 0; top: 0; width: 306px; height: 256px;
    background: radial-gradient(ellipse at 75% 30%, var(--leaf) 0%, rgba(31,58,44,0.5) 45%, rgba(31,58,44,0) 75%);
  }
  .fruit-art {
    position: absolute; left: 0; bottom: 0; width: 500px; height: 135px;
    background: linear-gradient(180deg, rgba(42,49,66,0) 0%, var(--berry-blue) 45%, var(--berry-red) 100%);
  }
  .title-main, .title-sub { position: absolute; font-family: "Pinyon Script", cursive; font-weight: 400; line-height: 1; white-space: nowrap; }
  .title-main { left: 40px; top: 40px; font-size: 112px; color: var(--yellow); }
  .title-sub { left: 158px; top: 150px; font-size: 86px; color: var(--white); }
  .rule { position: absolute; width: 2px; background: var(--white); }
  .section-band {
    position: absolute; left: 78px; width: 338px; height: 62px; background: var(--yellow);
    clip-path: polygon(3% 8%, 97% 0, 100% 35%, 98% 70%, 100% 100%, 4% 96%, 0 65%, 2% 30%);
    display: flex; align-items: center; justify-content: center;
    font-weight: 800; font-size: 33px; color: var(--ink); letter-spacing: 0.5px;
  }
  .price-list { position: absolute; left: 103px; width: 292px; list-style: none; }
  .price-row {
    display: flex; justify-content: space-between; height: 56.5px; align-items: center;
    font-style: italic; font-weight: 700; font-size: 26px; color: var(--yellow); text-transform: uppercase;
  }
  .price-row .price { color: var(--white); }
  .icons { position: absolute; top: 1090px; left: 180px; display: flex; gap: 38px; }
</style>
</head>
<body>
<main class="menu-panel">
  <div class="leaf-art" role="img" aria-label="Cannabis leaves in the top corner"></div>
  <div class="fruit-art" role="img" aria-label="Strawberries and blueberries along the bottom"></div>

  <h1 class="title-main">Cannabis</h1>
  <h2 class="title-sub">Menu</h2>

  <span class="rule" style="left:450px; top:125px; height:416px;"></span>
  <span class="rule" style="left:460px; top:140px; height:380px;"></span>
  <span class="rule" style="left:35px; top:697px; height:409px;"></span>
  <span class="rule" style="left:46px; top:720px; height:370px;"></span>

  <div class="section-band" style="top:284px;">WEED P/G</div>
  <ul class="price-list" style="top:346px;">
    <li class="price-row"><span>Vortigan</span><span class="price">€16</span></li>
    <li class="price-row"><span>Tangerosa</span><span class="price">€14</span></li>
    <li class="price-row"><span>Dusk Rover</span><span class="price">€14</span></li>
    <li class="price-row"><span>Mangolina</span><span class="price">€16</span></li>
    <li class="price-row"><span>Ultra Fern</span><span class="price">€14</span></li>
    <li class="price-row"><span>Amber Hermit</span><span class="price">€14</span></li>
  </ul>

  <div class="section-band" style="top:746px;">HASH P/G</div>
  <ul class="price-list" style="top:816px;">
    <li class="price-row"><span>Nepali Bronze</span><span class="price">€12</span></li>
    <li class="price-row"><span>Velvet Ember</span><span class="price">€11</span></li>
    <li class="price-row"><span>Cedar Pine</span><span class="price">€14</span></li>
    <li class="price-row"><span>Red Fable</span><span class="price">€10</span></li>
  </ul>

  <div class="icons">
    <svg width="52" height="52" viewBox="0 0 52 52" role="img" aria-label="Cannabis leaf sign">
      <circle cx="26" cy="26" r="25" fill="#f2ec1f"/>
      <g fill="#1b2024">
        <ellipse cx="26" cy="20" rx="3.2" ry="12"/>
        <ellipse cx="26" cy="20" rx="2.6" ry="10" transform="rotate(-38 26 30)"/>
        <ellipse cx="26" cy="20" rx="2.6" ry="10" transform="rotate(38 26 30)"/>
        <ellipse cx="26" cy="22" rx="2" ry="8" transform="rotate(-72 26 30)"/>
        <ellipse cx="26" cy="22" rx="2" ry="8" transform="rotate(72 26 30)"/>
        <rect x="25.2" y="30" width="1.6" height="10"/>
      </g>
    </svg>
    <svg width="52" height="52" viewBox="0 0 52 52" role="img" aria-label="No cigarettes allowed">
      <circle cx="26" cy="26" r="25" fill="#f2ec1f"/>
      <circle cx="26" cy="26" r="18" fill="none" stroke="#1b2024" stroke-width="4"/>
      <rect x="12" y="25" width="22" height="6" fill="#1b2024"/>
      <rect x="35" y="25" width="4" height="6" fill="#1b2024"/>
      <path d="M36 22 q-3 -4 1 -8" fill="none" stroke="#1b2024" stroke-width="2"/>
      <line x1="13" y1="13" x2="39" y2="39" stroke="#1b2024" stroke-width="4"/>
    </svg>
  </div>
</main>
</body>
</html>
```